Maison Corvel

I am actually making my own traditional french food.
Everything is homemade with passion.
I make differente terrines, jams, macaroons, rillettes and much more
I do as well cocktail party and catering
Updates

Hello everyone,

On the business card I would like to see appear if it's possible these following informations: traditional french food, cocktail party and catering.

Industry/Entity Type

Catering

```html
<!DOCTYPE html>
<html lang="en">
<head>
<meta charset="utf-8">
<title>Maison Corvel – Business Card</title>
<link href="https://fonts.googleapis.com/css2?family=Cinzel:wght@400;600&family=Arimo:wght@400;700&display=swap" rel="stylesheet">
<style>
  :root {
    --backdrop: #e8e3db;
    --card: #ffffff;
    --navy: #2e3192;
    --red: #d2232a;
    --ink: #231f20;
    --white: #ffffff;
  }
  * { margin: 0; padding: 0; box-sizing: border-box; }
  html, body {
    width: 1088px;
    height: 1200px;
    overflow: hidden;
    background: var(--backdrop);
  }
  .canvas { position: relative; width: 1088px; height: 1200px; }

  .card {
    position: absolute;
    background: var(--card);
    border-radius: 33px;
    overflow: hidden;
    box-shadow: 0 2px 6px rgba(0,0,0,0.15);
  }
  .card--front { left: 117px; top: 75px; width: 879px; height: 501px; }
  .card--back  { left: 110px; top: 629px; width: 875px; height: 498px; }

  .front-waves { position: absolute; inset: 0; width: 100%; height: 100%; }

  .brand-name {
    position: absolute;
    left: 0; width: 100%;
    font-family: "Arimo", sans-serif;
    font-weight: 700;
    color: var(--ink);
    text-align: center;
    white-space: nowrap;
  }
  .card--front .brand-name { top: 196px; font-size: 34px; }
  .card--back .brand-name { top: 190px; font-size: 48px; }

  .holder-name {
    position: absolute;
    left: 142px; top: 408px;
    font-family: "Arimo", sans-serif;
    font-weight: 700; font-size: 31px;
    color: var(--white);
  }
  .divider {
    position: absolute;
    left: 437px; top: 370px;
    width: 2px; height: 106px;
    background: var(--white);
  }
  .contact-list {
    position: absolute;
    left: 456px; top: 368px;
    list-style: none;
    font-family: "Arimo", sans-serif;
    font-size: 22px;
    color: var(--white);
  }
  .contact-list li { display: flex; align-items: center; height: 40px; gap: 8px; }
  .contact-list svg { width: 18px; height: 18px; fill: var(--white); }

  .services {
    position: absolute;
    left: 0; width: 100%; top: 392px;
    font-family: "Cinzel", serif;
    font-size: 25px;
    color: var(--ink);
    text-align: center;
  }
  .services p { height: 44px; line-height: 44px; }
  .services span { display: inline-flex; align-items: center; gap: 8px; margin: 0 14px; }
  .bullet { width: 12px; height: 12px; border-radius: 50%; background: var(--red); display: inline-block; }
</style>
</head>
<body>
<main class="canvas">

  <section class="card card--front">
    <svg class="front-waves" viewBox="0 0 527 300" preserveAspectRatio="none" aria-hidden="true">
      <path fill="var(--red)" d="M0 108 C 110 168, 260 200, 425 186 C 320 206, 140 190, 0 134 Z"/>
      <path fill="var(--navy)" d="M0 146 C 120 192, 250 214, 340 206 C 420 198, 480 172, 527 146 L527 300 L0 300 Z"/>
    </svg>

    <div class="brand-name">Maison Corvel</div>

    <div class="holder-name">Julien Marchand</div>
    <div class="divider"></div>
    <ul class="contact-list">
      <li>
        <svg viewBox="0 0 24 24"><path d="M6.6 10.8a15.1 15.1 0 0 0 6.6 6.6l2.2-2.2c.3-.3.7-.4 1-.2 1.1.4 2.3.6 3.6.6.6 0 1 .4 1 1V20c0 .6-.4 1-1 1C10.6 21 3 13.4 3 4c0-.6.4-1 1-1h3.5c.6 0 1 .4 1 1 0 1.3.2 2.5.6 3.6.1.3 0 .7-.2 1z"/></svg>
        0412 555 018
      </li>
      <li>
        <svg viewBox="0 0 24 24"><path d="M2 5h20v14H2z M4 7v.5l8 5 8-5V7z" fill-rule="evenodd"/></svg>
        julien@corvel.fr
      </li>
      <li>ABN:51824753609</li>
    </ul>
  </section>

  <section class="card card--back">
    <div class="brand-name">Maison Corvel</div>
    <div class="services">
      <p><span><i class="bullet"></i>Traditional French Food</span></p>
      <p><span><i class="bullet"></i>Cocktail Party</span><span><i class="bullet"></i>Catering</span></p>
    </div>
  </section>

</main>
</body>
</html>
```